Business card for Bio pharmaceutical company

Hello,
We are a bio pharmaceutical contract manufacturing company in Brisbane, Australia. Can you please create a new business card design. Please go to our website for colours http://www.velocrine.com.au.
On the back can you include the cartoon mascot Tobin Wuzzle and the tagline
"A Global Biopharmaceutical Contract Development Manufacturing Company"
Target Market(s)
Biotechnology
Industry/Entity Type
Pharmaceutical
Contact Information for Business Card
Maria Hollingby
Business Development Manager
maria.hollingby@velocrine.com.au
1947 Kelmott Street Parvale Queesnland 4213 Australia
T: +61 7 3590 2481
M +61 427 516 093
F +61 7 3648 2057
www.velocrine.com.au
Look and feel

```html
<!DOCTYPE html>
<html lang="en">
<head>
<meta charset="utf-8">
<title>Velocrine business card</title>
<link rel="stylesheet" href="https://fonts.googleapis.com/css2?family=Open+Sans:wght@400;600;700&display=swap">
<style>
  :root {
    --backdrop: #ece9e4;
    --card: #ffffff;
    --card-edge: #e4e4e4;
    --brand-blue: #1c5a8a;
    --ink: #3b3f45;
    --lime: #b9cf2d;
    --lime-soft: #d4e06a;
    --mascot-blue: #6cc3e3;
    --mascot-deep: #2c7fa8;
  }
  * { box-sizing: border-box; margin: 0; padding: 0; }
  html, body { width: 1200px; height: 1023px; overflow: hidden; }
  body {
    background: var(--backdrop);
    font-family: "Open Sans", Arial, sans-serif;
    color: var(--ink);
    position: relative;
  }
  .card {
    position: absolute;
    width: 540px;
    height: 320px;
    background: var(--card);
    border-radius: 22px;
    box-shadow: 0 2px 0 var(--card-edge), 0 14px 30px rgba(0,0,0,.18);
    overflow: hidden;
  }
  .card--front { left: 50px; top: 90px; }
  .card--back { left: 610px; top: 590px; }

  .swoosh { position: absolute; inset: 0; width: 100%; height: 100%; }

  .pattern {
    position: absolute;
    background: radial-gradient(circle at 40% 40%, var(--lime-soft), var(--lime));
  }
  .card--front .pattern { right: 0; top: 0; width: 170px; height: 100px; border-radius: 0 22px 0 60px; }
  .card--back .pattern { right: 0; bottom: 0; width: 160px; height: 90px; border-radius: 60px 0 22px 0; }

  .wordmark {
    font-weight: 700;
    color: var(--brand-blue);
    letter-spacing: -0.5px;
    display: flex;
    align-items: center;
    gap: 8px;
    line-height: 1.2;
  }
  .wordmark__dot { width: 12px; height: 12px; background: var(--brand-blue); border-radius: 2px; }
  .card--front .wordmark { position: absolute; left: 30px; top: 112px; font-size: 44px; }

  .address {
    position: absolute; right: 28px; top: 186px;
    font-style: normal;
    font-size: 12.5px; line-height: 1.45; text-align: right; color: var(--brand-blue);
  }
  .person { position: absolute; left: 34px; top: 206px; }
  .person__name { font-size: 17px; font-weight: 700; color: var(--brand-blue); }
  .person__title { font-size: 11.5px; color: var(--lime); font-weight: 600; }

  .contacts { position: absolute; left: 230px; top: 230px; list-style: none; font-size: 11.5px; line-height: 1.55; color: var(--brand-blue); }
  .contacts li { display: flex; align-items: center; gap: 7px; }
  .contacts svg { width: 11px; height: 11px; flex: none; }

  .card--back .wordmark { position: absolute; left: 30px; top: 34px; font-size: 28px; }
  .tagline-art {
    position: absolute; left: 30px; top: 80px; width: 160px; height: 26px;
    background: linear-gradient(90deg, var(--mascot-deep), var(--brand-blue));
    border-radius: 13px; opacity: .85;
  }
  .mascot {
    position: absolute; left: 250px; top: 22px; width: 200px; height: 120px;
    background: radial-gradient(ellipse at center, var(--mascot-blue), var(--mascot-deep));
    border-radius: 60px;
  }
  .statement {
    position: absolute; left: 252px; top: 168px; width: 260px;
    font-size: 13px; line-height: 1.45; color: var(--brand-blue);
  }
</style>
</head>
<body>
  <section class="card card--front" aria-label="Card front">
    <svg class="swoosh" viewBox="0 0 540 320" aria-hidden="true">
      <path d="M220 218 Q 360 198 540 102 L540 111 Q 360 204 220 218 Z" fill="var(--lime)"/>
    </svg>
    <div class="pattern" role="img" aria-label="Lime dotted decorative pattern"></div>
    <address class="address">1947 Kelmott Street<br>Parvale Queesnland 4213<br>Australia</address>
    <div class="wordmark"><span>Velocrine</span><span class="wordmark__dot"></span></div>
    <div class="person">
      <p class="person__name">Maria Hollingby</p>
      <p class="person__title">Business Development Manager</p>
    </div>
    <ul class="contacts">
      <li><svg viewBox="0 0 11 11"><rect width="11" height="11" rx="2" fill="var(--lime)"/><path d="M3 2.5h2l.5 2-1 .8a5 5 0 0 0 1.7 1.7l.8-1 2 .5v2A1 1 0 0 1 8 9.5 6.5 6.5 0 0 1 2 3.5a1 1 0 0 1 1-1z" fill="#fff"/></svg>+61 7 3590 2481</li>
      <li><svg viewBox="0 0 11 11"><rect width="11" height="11" rx="2" fill="var(--lime)"/><rect x="3.5" y="2" width="4" height="7" rx="1" fill="#fff"/></svg>+61 427 516 093</li>
      <li><svg viewBox="0 0 11 11"><rect width="11" height="11" rx="2" fill="var(--lime)"/><rect x="2.5" y="4" width="6" height="4" fill="#fff"/><rect x="3.5" y="2" width="4" height="2" fill="#fff"/></svg>+61 7 3648 2057</li>
      <li><svg viewBox="0 0 11 11"><rect width="11" height="11" rx="2" fill="var(--lime)"/><rect x="2" y="3" width="7" height="5" fill="#fff"/><path d="M2 3l3.5 3L9 3" stroke="var(--lime)" fill="none"/></svg>maria.hollingby@velocrine.com.au</li>
      <li><svg viewBox="0 0 11 11"><rect width="11" height="11" rx="2" fill="var(--lime)"/><circle cx="5.5" cy="5.5" r="3" fill="none" stroke="#fff"/></svg>www.velocrine.com.au</li>
    </ul>
  </section>

  <section class="card card--back" aria-label="Card back">
    <svg class="swoosh" viewBox="0 0 540 320" aria-hidden="true">
      <path d="M238 170 Q 250 262 326 320 L338 320 Q 256 258 238 170 Z" fill="var(--lime)"/>
    </svg>
    <div class="wordmark"><span>Velocrine</span><span class="wordmark__dot"></span></div>
    <div class="tagline-art" role="img" aria-label="Hand-lettered tagline"></div>
    <div class="mascot" role="img" aria-label="Cartoon mascot Tobin Wuzzle, a blue bacterium character"></div>
    <p class="statement">A Global Biopharmaceutical Contract Development Manufacturing Company</p>
    <div class="pattern" role="img" aria-label="Lime dotted decorative pattern"></div>
  </section>
</body>
</html>
```